professional business card design for technology company

We are a small technology consulting firm, specialising in consulting based around Cloud and Managed services. Our colour scheme is yellow, blue and white, as you can see in the logos. Although we are based in melbourne australia, due to the nature of our work, our clients can be located anywhere. We are looking for a clean, professional, positive look - similar to our company logo

Target Market(s)

small business

Industry/Entity Type

Business

Contact Information for Business Card

eye catching, designed to incorporate some level of raised printing. Must contain website address, phone number, name and job title

Requirements
Must have
• Logo (attached) - use of the same colour scheme

```html
<!DOCTYPE html>
<html lang="en">
<head>
<meta charset="utf-8">
<title>Nimbara Business Card</title>
<link rel="stylesheet" href="https://fonts.googleapis.com/css2?family=Exo+2:ital,wght@0,400;0,500;0,600;1,400&display=swap">
<style>
  :root {
    --backdrop: #e6e7e8;
    --card-white: #f7f7f7;
    --band-grey: #5f6062;
    --accent-yellow: #ffd21f;
    --brand-blue: #3aa6e0;
    --ink-dark: #4a4b4d;
    --ink-soft: #5c5d60;
    --text-light: #ffffff;
  }
  * { margin: 0; padding: 0; box-sizing: border-box; }
  html, body {
    width: 1200px;
    height: 899px;
    overflow: hidden;
    background: var(--backdrop);
    font-family: "Exo 2", sans-serif;
  }
  .business-card {
    position: absolute;
    left: 100px;
    top: 150px;
    width: 1000px;
    height: 600px;
    border-radius: 44px;
    overflow: hidden;
    background: var(--card-white);
    box-shadow: 0 10px 30px rgba(0,0,0,0.18);
  }
  .card-art {
    position: absolute;
    inset: 0;
    width: 1000px;
    height: 600px;
  }
  .holder {
    position: absolute;
    right: 50px;
    top: 70px;
    text-align: right;
    color: var(--text-light);
  }
  .holder-name {
    font-size: 38px;
    font-weight: 500;
    letter-spacing: 2px;
    text-transform: uppercase;
  }
  .holder-title {
    font-size: 24px;
    font-weight: 400;
    margin-top: 4px;
  }
  .brand {
    position: absolute;
    left: 60px;
    top: 205px;
    display: flex;
    align-items: center;
    gap: 20px;
  }
  .brand-dot {
    width: 58px;
    height: 58px;
    border-radius: 50%;
    background: var(--brand-blue);
  }
  .brand-name {
    font-size: 86px;
    font-weight: 600;
    color: var(--ink-soft);
    line-height: 1;
  }
  .contact-list {
    position: absolute;
    left: 42px;
    top: 330px;
    list-style: none;
  }
  .contact-list li {
    display: flex;
    align-items: center;
    gap: 14px;
    height: 40px;
    font-size: 21px;
    color: var(--ink-dark);
  }
  .contact-list svg {
    width: 20px;
    height: 20px;
    fill: var(--ink-dark);
  }
  .contact-list .web { font-size: 17px; }
  .address {
    position: absolute;
    right: 50px;
    bottom: 62px;
    text-align: right;
    font-size: 22px;
    font-style: italic;
    color: var(--ink-dark);
    line-height: 1.35;
  }
</style>
</head>
<body>
  <section class="business-card">
    <svg class="card-art" viewBox="0 0 1000 600" aria-hidden="true">
      <path d="M0,0 H1000 V330 C820,175 420,115 0,165 Z" fill="var(--band-grey)"/>
      <path d="M0,165 C420,115 820,175 1000,330 V352 C820,200 420,140 0,182 Z" fill="var(--accent-yellow)"/>
    </svg>

    <div class="holder">
      <p class="holder-name">Marcus Delane</p>
      <p class="holder-title">Managing Director</p>
    </div>

    <div class="brand">
      <span class="brand-dot"></span>
      <span class="brand-name">Nimbara</span>
    </div>

    <ul class="contact-list">
      <li>
        <svg viewBox="0 0 20 20"><path d="M5 2h4l1.5 4-2 1.5a10 10 0 0 0 4 4L14 9.5l4 1.5v4a2 2 0 0 1-2 2A14 14 0 0 1 3 4a2 2 0 0 1 2-2z"/></svg>
        <span>015 550 0142</span>
      </li>
      <li>
        <svg viewBox="0 0 20 20"><rect x="5" y="1" width="10" height="18" rx="2"/><rect x="7" y="3.5" width="6" height="11" fill="var(--card-white)"/></svg>
        <span>015 550 0143</span>
      </li>
      <li>
        <svg viewBox="0 0 20 20"><rect x="2" y="7" width="16" height="11" rx="1.5"/><rect x="5" y="2" width="10" height="6"/></svg>
        <span>015 550 0144</span>
      </li>
      <li>
        <svg viewBox="0 0 20 20"><rect x="1" y="4" width="18" height="12" rx="1.5"/><path d="M2 5l8 6 8-6" stroke="var(--card-white)" stroke-width="1.6" fill="none"/></svg>
        <span class="web">hello@nimbara.net</span>
      </li>
      <li>
        <svg viewBox="0 0 20 20"><circle cx="10" cy="10" r="8.5"/><path d="M1.5 10h17M10 1.5c-4 4.5-4 12.5 0 17M10 1.5c4 4.5 4 12.5 0 17" stroke="var(--card-white)" stroke-width="1.3" fill="none"/></svg>
        <span class="web">www.nimbara.net</span>
      </li>
    </ul>

    <p class="address">41 Harbour Lane, Level 6<br>Carlton VIC</p>
  </section>
</body>
</html>
```